Construction company that specializes in roofing and siding

https://havenridgeroofs.example/featured-projects/

https://www.pinecrestrenovationllc.example/#

https://www.ironmeadowhomes.example/residential-siding-services/

Please model a website after these examples
I posted a doc that has some content to get you started. I will upload more content and photos as the site progresses.

Coded - Design and coding required

5+ page

```html
<!DOCTYPE html>
<html lang="en">
<head>
<meta charset="utf-8">
<title>Stoneway Construction</title>
<link rel="stylesheet" href="https://fonts.googleapis.com/css2?family=Audiowide&family=Lexend:wght@400;500&family=Roboto:wght@400;500;700&display=swap">
<style>
:root{
  --ink:#1e1e1e;
  --text:#2b2b2b;
  --muted:#555;
  --line:#e3e3e3;
  --pill:#5c5c5c;
  --pill-dark:#4a4a4a;
  --band:#48484a;
  --soft:#ececec;
  --white:#fff;
}
*{box-sizing:border-box;margin:0;padding:0}
html,body{width:1200px;height:3705px;overflow:hidden;background:var(--white);font-family:"Roboto",Arial,sans-serif;color:var(--text)}
.page{position:relative;width:1200px;height:3705px}

.topbar{height:43px;background:linear-gradient(#f6f6f6,#e6e6e6);display:flex;align-items:center;padding:0 98px;font-size:14px}
.topbar .item{display:flex;align-items:center;gap:10px;margin-right:60px}
.icon-dot{width:26px;height:26px;border-radius:50%;background:var(--ink);display:flex;align-items:center;justify-content:center}
.socials{margin-left:auto;display:flex;gap:12px}
.socials span{width:28px;height:28px;border-radius:50%;background:var(--ink)}

.nav{height:87px;display:flex;align-items:center;padding:0 98px;border-bottom:1px solid var(--line)}
.brand{display:flex;align-items:center;gap:12px;font-family:"Audiowide",sans-serif;font-size:24px;color:#3a3a3a;letter-spacing:1px}
.brand .mark{width:26px;height:26px;background:#4a4a4a}
.menu{margin-left:auto;display:flex;gap:24px;font-family:"Lexend",sans-serif;font-size:16px;font-weight:500;color:var(--ink)}
.menu span.drop::after{content:" ⌄";font-size:12px}

.hero{position:relative;height:597px;background:linear-gradient(100deg,#5a5c60 0%,#7b7e82 45%,#a9adb2 75%,#c8cbd0 100%)}
.hero .title{position:absolute;left:96px;top:148px;font-family:"Audiowide",sans-serif;color:var(--white);line-height:1}
.hero .title .l1{font-size:64px;letter-spacing:3px}
.hero .title .l2{font-size:42px;letter-spacing:3px;margin-top:16px}
.hero p{position:absolute;left:98px;top:285px;width:440px;color:#f0f0f0;font-size:15px;line-height:30px;font-family:"Roboto",serif}
.hero .cta{position:absolute;left:98px;top:397px;width:126px;height:43px;border-radius:22px;background:var(--white);color:#555;font-size:16px;display:flex;align-items:center;justify-content:center}
.arrow{position:absolute;top:284px;width:32px;height:32px;border:1.5px solid #fff;border-radius:50%;display:flex;align-items:center;justify-content:center}
.arrow.prev{left:29px}.arrow.next{right:29px}

.about{position:relative;height:614px}
.section-h{font-family:"Audiowide",sans-serif;font-size:32px;color:#444;letter-spacing:2px}
.about .section-h{position:absolute;left:97px;top:86px}
.about h3{position:absolute;left:98px;top:138px;font-size:19px;font-weight:500;color:var(--ink)}
.about p{position:absolute;left:98px;top:172px;width:470px;font-size:14.5px;line-height:30px}
.btn{display:inline-flex;align-items:center;justify-content:center;height:40px;padding:0 24px;border-radius:20px;background:var(--pill);color:var(--white);font-size:15px;font-weight:500}
.about .btn{position:absolute;left:98px;top:432px}
.about .photo{position:absolute;left:622px;top:92px;width:479px;height:390px;border-radius:12px;background:linear-gradient(160deg,#c4c8cb 0%,#55585c 45%,#3b3d40 70%,#8d9a7e 100%)}

.services{position:relative;height:1525px;background:linear-gradient(#e9e9e9,#f6f6f6)}
.services .section-h{position:absolute;left:0;right:0;top:90px;text-align:center}
.tabs{position:absolute;top:164px;left:0;right:0;display:flex;justify-content:center;gap:28px}
.tab{height:46px;border:1.5px solid #555;border-radius:23px;display:flex;align-items:center;justify-content:center;font-size:17px;color:var(--ink);background:#f2f2f2}
.tab.active{background:var(--pill);border-color:var(--pill);color:var(--white);font-size:18px}
.svc-photo{position:absolute;width:467px;height:347px;border-radius:12px;box-shadow:0 4px 10px rgba(0,0,0,.25)}
.svc-text{position:absolute;width:450px}
.svc-text h4{font-family:"Audiowide",sans-serif;font-size:26px;color:var(--ink);margin-bottom:26px}
.svc-text p{font-size:14.5px;line-height:30px;margin-bottom:30px}
.svc-text.right{text-align:right}

.promise{height:382px;background:var(--band);color:var(--white);text-align:center;padding-top:80px}
.promise h2{font-family:"Audiowide",sans-serif;font-size:30px;letter-spacing:2px;margin-bottom:26px}
.promise p{font-size:16.5px;font-weight:700;line-height:30px}
.promise .sign{margin-top:30px}

.footer{position:relative;height:457px}
.footer .brand{position:absolute;left:0;right:0;top:106px;justify-content:center;font-size:34px}
.footer .brand .mark{width:36px;height:36px}
.flinks{position:absolute;top:218px;left:0;right:0;display:flex;justify-content:center;gap:36px;font-size:17px;color:#333}
.contacts{position:absolute;top:290px;left:137px;right:80px;display:flex;justify-content:space-between;align-items:center;font-size:15px}
.contacts .c{display:flex;align-items:center;gap:16px}
.sq{width:49px;height:49px;background:#6a6a6a;display:flex;align-items:center;justify-content:center}
.copy{position:absolute;top:390px;left:0;right:0;text-align:center;font-size:16px;color:#333}
</style>
</head>
<body>
<div class="page">

<header class="topbar">
  <div class="item"><span class="icon-dot"><svg width="13" height="13" viewBox="0 0 24 24"><path fill="#fff" d="M6.6 10.8a15 15 0 006.6 6.6l2.2-2.2c.3-.3.7-.4 1-.2 1.1.4 2.3.6 3.6.6.6 0 1 .4 1 1V20c0 .6-.4 1-1 1A17 17 0 013 4c0-.6.4-1 1-1h3.5c.6 0 1 .4 1 1 0 1.3.2 2.5.6 3.6.1.3 0 .7-.2 1z"/></svg></span>+1 555 0142 3380</div>
  <div class="item"><span class="icon-dot"><svg width="13" height="10" viewBox="0 0 24 18"><rect width="24" height="18" rx="2" fill="#fff"/><path d="M1 2l11 8 11-8" stroke="#1e1e1e" stroke-width="2" fill="none"/></svg></span>info@stonewayconstruction.example</div>
  <div class="socials"><span></span><span></span><span></span><span></span></div>
</header>

<nav class="nav">
  <div class="brand"><span class="mark"></span>STONEWAY CONSTRUCTION</div>
  <div class="menu"><span>Home</span><span class="drop">Roofing</span><span class="drop">Siding</span><span>Gutters</span><span>Windows</span><span class="drop">Repair</span><span class="drop">Contact Us</span></div>
</nav>

<section class="hero" role="img" aria-label="Two roofers in hard hats nailing shingles on a roof">
  <div class="title"><div class="l1">STONEWAY</div><div class="l2">CONSTRUCTION</div></div>
  <p>In 2016 Dale Harper started helping people with their home improvement projects. His very first job was installing window trim for a wonderful homeowner in Forest lake MN.</p>
  <div class="cta">Get Started</div>
  <div class="arrow prev"><svg width="10" height="14"><path d="M8 1L2 7l6 6" stroke="#fff" stroke-width="1.6" fill="none"/></svg></div>
  <div class="arrow next"><svg width="10" height="14"><path d="M2 1l6 6-6 6" stroke="#fff" stroke-width="1.6" fill="none"/></svg></div>
</section>

<section class="about">
  <h2 class="section-h">ABOUT US</h2>
  <h3>From humble beginnings:</h3>
  <p>In 2016 Dale Harper started helping people with their home improvement projects. His very first job was installing window trim for a wonderful homeowner in Forest lake MN. He did his best work and made sure he treated his first customer like family. Afterall, his first customer was Ruth Harper, his Mom. Today, Dale and the Stoneway Construction team are helping homeowners around <b>Minnesota;</b> carrying the spirit of his first job onto every job they touch.</p>
  <span class="btn">Read More</span>
  <div class="photo" role="img" aria-label="Dark tiled roof with a brick chimney against the sky"></div>
</section>

<section class="services">
  <h2 class="section-h">OUR SERVICES</h2>
  <div class="tabs">
    <span class="tab" style="width:132px">Roofing</span>
    <span class="tab" style="width:132px">Siding</span>
    <span class="tab active" style="width:264px">Storm damage repair</span>
    <span class="tab" style="width:132px">Gutters</span>
    <span class="tab" style="width:132px">Repair</span>
  </div>

  <div class="svc-photo" style="left:98px;top:279px;background:linear-gradient(135deg,#6e7073,#3c3e41 55%,#5a5c5f)" role="img" aria-label="Gloved hand lifting a wind-damaged shingle"></div>
  <div class="svc-text" style="left:639px;top:300px">
    <h4>Wind damage repair</h4>
    <p>If you are missing roofing or siding after a storm, the first step is to have a licensed and insured professional evaluate and document the damage.</p>
    <p>Then a temporary repair should be performed to keep your home or business dry during the insurance claim process. Stoneway Construction specializes in wind damage assessment and repair.</p>
    <span class="btn">Read More</span>
  </div>

  <div class="svc-text right" style="left:97px;top:703px">
    <h4>Hail damage repair</h4>
    <p>If you are missing roofing or siding after a storm, the first step is to have a licensed and insured professional evaluate and document the damage.</p>
    <p>Then a temporary repair should be performed to keep your home or business dry during the insurance claim process. Stoneway Construction specializes in wind damage assessment and repair.</p>
    <span class="btn">Read More</span>
  </div>
  <div class="svc-photo" style="left:622px;top:682px;background:linear-gradient(160deg,#5f7a46 0%,#6d6a66 30%,#8a8580 70%,#4c4a48)" role="img" aria-label="Aerial view of a hail-worn shingle roof"></div>

  <div class="svc-photo" style="left:98px;top:1085px;background:linear-gradient(180deg,#555658,#2f3032 50%,#58595b)" role="img" aria-label="Weathered wood shingles with a hole from tree impact"></div>
  <div class="svc-text" style="left:639px;top:1106px">
    <h4>Tree damage repair</h4>
    <p>If you are missing roofing or siding after a storm, the first step is to have a licensed and insured professional evaluate and document the damage.</p>
    <p>Then a temporary repair should be performed to keep your home or business dry during the insurance claim process. Stoneway Construction specializes in wind damage assessment and repair.</p>
    <span class="btn">Read More</span>
  </div>
</section>

<section class="promise">
  <h2>THE STONEWAY PROMISE</h2>
  <p>You deserve timely service, high quality materials, expert installation, and a solid<br>warranty. That is what we promise to deliver. I invite you to put us to the test today.</p>
  <p class="sign">Sincerely,<br>Dale Harper, Owner<br>Stoneway Construction</p>
</section>

<footer class="footer">
  <div class="brand"><span class="mark"></span>STONEWAY CONSTRUCTION</div>
  <div class="flinks"><span>Home</span><span>Roofing</span><span>Siding</span><span>Gutters</span><span>Windows</span><span>Repair</span><span>Contact Us</span></div>
  <div class="contacts">
    <div class="c"><span class="sq"><svg width="22" height="16" viewBox="0 0 24 18"><rect width="24" height="18" rx="1" fill="#fff"/><path d="M1 1l11 8 11-8" stroke="#6a6a6a" stroke-width="2" fill="none"/></svg></span>info@stonewayconstruction.example</div>
    <div class="c"><span class="sq"><svg width="16" height="22" viewBox="0 0 16 22"><path d="M8 0a8 8 0 00-8 8c0 6 8 14 8 14s8-8 8-14a8 8 0 00-8-8z" fill="#fff"/><circle cx="8" cy="8" r="3" fill="#6a6a6a"/></svg></span>Stoneway Construction, United States.</div>
    <div class="c"><span class="sq"><svg width="20" height="20" viewBox="0 0 24 24"><path fill="#fff" d="M6.6 10.8a15 15 0 006.6 6.6l2.2-2.2c.3-.3.7-.4 1-.2 1.1.4 2.3.6 3.6.6.6 0 1 .4 1 1V20c0 .6-.4 1-1 1A17 17 0 013 4c0-.6.4-1 1-1h3.5c.6 0 1 .4 1 1 0 1.3.2 2.5.6 3.6.1.3 0 .7-.2 1z"/></svg></span><span style="font-size:17px">+1 555 0142 338</span></div>
  </div>
  <div class="copy">Copyrights@2024.Stoneway Construction.All Rights Reserved</div>
</footer>

</div>
</body>
</html>
```